Neues Design für die Homepage eines Taekwondo-Vereins
Zielgruppe
Der Kampfsportgilde Rheinau ist ein Taekwondo-Verein für die ganze Familie. Trainieren können bei uns Kinder ab 5 Jahren ebenso wie Erwachsene. Wir betreiben Breitensport, es steht für uns also nicht der Wettkampf sondern die persönliche Entwicklung unserer Mitglieder im Vordergrund.
Aufgabenstellung
Wichtig ist uns eine vertikale Menüleiste. Das Menü besteht aus Ober- und Unterpunkten. Bitte berücksichtigen Sie dies bei der Layoutgestaltung. Das Impressum sollte im Footer platziert werden. Außerdem sollte die Möglichkeit der Einbindung von Social Media Buttons gegeben sein.
Das Layout der Seite sollte aufgeräumt, aber dennoch einladend sein. Das Design soll das Interesse des Besuchers wecken und dafür sorgen, dass er sich auf Anhieb wohl fühlt.
Wir hätten gerne auf der Startseite vier Teaserkästen, die jeweils aus einem Bild und Text bestehen.
Großen Wert legen wir auf die Tatsache, dass die Seite responsive ist. Das Layout soll für das CMS Wordpress geeignet sein.

```html
<!DOCTYPE html>
<html lang="de">
<head>
<meta charset="utf-8">
<title>Kampfsportgilde Rheinau – Home</title>
<link href="https://fonts.googleapis.com/css2?family=Roboto:wght@300;400;500&display=swap" rel="stylesheet">
<style>
  :root{
    --page:#f0f0f0;
    --panel:#ffffff;
    --accent:#df4219;
    --heading:#4a4a4a;
    --body:#7a7a7a;
    --rule:#d9d9d9;
    --social:#3b5998;
  }
  *{margin:0;padding:0;box-sizing:border-box}
  html,body{width:1200px;height:741px;overflow:hidden;background:var(--page);font-family:'Roboto',sans-serif}
  .canvas{position:relative;width:1200px;height:741px}
  .panel{position:absolute;background:var(--panel)}

  .sidebar{left:244px;top:13px;width:169px;height:319px;text-align:center}
  .brand{position:absolute;left:0;right:0;top:20px;display:flex;flex-direction:column;align-items:center;gap:6px}
  .brand-dot{width:26px;height:26px;border-radius:50%;background:var(--accent)}
  .brand-name{font-size:10px;font-weight:500;color:var(--heading);line-height:1.25}
  .rule{position:absolute;left:28px;width:113px;height:1px;background:var(--rule)}
  .main-nav{position:absolute;left:0;right:0;top:116px;list-style:none}
  .main-nav li{height:22.6px;font-size:10px;font-weight:500;color:var(--heading);letter-spacing:.1px}
  .main-nav li.active{color:var(--accent)}
  .social{position:absolute;left:72px;top:281px;width:25px;height:25px;border-radius:50%;background:var(--social)}

  .hero{left:425px;top:13px;width:531px;height:319px}
  .hero-media{position:absolute;left:12.5px;top:12.5px;width:506px;height:294px;
    background:radial-gradient(ellipse at 50% 55%,#efe6d4 0%,#d9c3a0 55%,#c79a6e 100%)}

  .about{left:244px;top:344px;width:712px;height:100px;text-align:center}
  .about h1{position:absolute;left:0;right:0;top:16px;font-size:12.5px;font-weight:500;color:var(--heading)}
  .about p{position:absolute;left:0;right:0;top:38px;font-size:10px;font-weight:300;color:var(--body);line-height:12.5px}
  .about .more{position:absolute;left:0;right:0;top:72px;font-size:10px;color:var(--accent)}

  .teaser{top:457px;width:169px;height:219px}
  .teaser-media{height:112.5px}
  .teaser h2{position:absolute;left:10px;top:121px;font-size:10px;font-weight:500;color:var(--heading)}
  .teaser p{position:absolute;left:10px;right:8px;top:139px;font-size:10px;font-weight:300;color:var(--body);line-height:12.5px}
  .teaser .more{position:absolute;left:10px;top:196px;font-size:10px;color:var(--heading)}
  .teaser .more.active{color:var(--accent)}

  .footer{left:244px;top:688px;width:712px;height:38px;font-size:10px;font-weight:300;color:var(--body)}
  .footer .copy{position:absolute;left:12px;top:13px}
  .footer .legal{position:absolute;right:12px;top:13px}
</style>
</head>
<body>
<div class="canvas">

  <aside class="panel sidebar">
    <div class="brand">
      <span class="brand-dot"></span>
      <span class="brand-name">Kampfsportgilde<br>Rheinau</span>
    </div>
    <div class="rule" style="top:99px"></div>
    <ul class="main-nav">
      <li class="active">HOME</li>
      <li>TAEKWONDO</li>
      <li>KALENDER</li>
      <li>BILDERGALERIE</li>
      <li>DOWNLOADS</li>
      <li>GÄSTEBUCH</li>
      <li>LINKS</li>
    </ul>
    <div class="rule" style="top:268px"></div>
    <span class="social" role="img" aria-label="Social-Media-Link"></span>
  </aside>

  <section class="panel hero">
    <div class="hero-media" role="img" aria-label="Foto: Hände zeigen auf das Vereinsabzeichen auf einem weißen Taekwondo-Anzug"></div>
  </section>

  <section class="panel about">
    <h1>ÜBER KAMPFSPORTGILDE RHEINAU</h1>
    <p>Der Kampfsportgilde Rheinau wurde 1990 von Sabum (Meister)Klaus Wender (Träger 6. Dan Taekwondo und 1. Dan Hapkido) gegründet.<br>Seit 1973 ist er im Taekwondosport aktiv, unter anderem als Bundesprüfer, Landeskampfrichter und natürlich Trainer.</p>
    <span class="more">READ MORE</span>
  </section>

  <article class="panel teaser" style="left:244px">
    <div class="teaser-media" role="img" aria-label="Foto: Kind im Taekwondo-Anzug beim Training mit Reifen" style="background:linear-gradient(160deg,#4f8fa8,#b08a5e)"></div>
    <h2>TRAINING FUER KINDER</h2>
    <p>Lorem Ipsum is simply dummy text of the printing and typesetting industry. Lorem Ipsum has been the industry's standard</p>
    <span class="more active">READ MORE</span>
  </article>

  <article class="panel teaser" style="left:425px">
    <div class="teaser-media" role="img" aria-label="Foto: Gruppe beim Taekwondo-Training in der Sporthalle" style="background:linear-gradient(180deg,#9aa9c0,#c9ccd0)"></div>
    <h2>SPORT FÜR DIE GANZE FAMILIE</h2>
    <p>Lorem Ipsum is simply dummy text of the printing and typesetting industry. Lorem Ipsum has been the industry's standard</p>
    <span class="more">READ MORE</span>
  </article>

  <article class="panel teaser" style="left:606px">
    <div class="teaser-media" role="img" aria-label="Foto: Mitglieder beim Dehnen auf dem Hallenboden" style="background:linear-gradient(180deg,#7f96b3,#b9bcc2)"></div>
    <h2>BREITENSPORT</h2>
    <p>Lorem Ipsum is simply dummy text of the printing and typesetting industry. Lorem Ipsum has been the industry's standard</p>
    <span class="more">READ MORE</span>
  </article>

  <article class="panel teaser" style="left:787px">
    <div class="teaser-media" role="img" aria-label="Foto: Tritttechnik gegen ein Schlagpolster in der Halle" style="background:linear-gradient(180deg,#a89a88,#c8a986)"></div>
    <h2>SELBSTVERTEIDIGUNG</h2>
    <p>Lorem Ipsum is simply dummy text of the printing and typesetting industry. Lorem Ipsum has been the industry's standard</p>
    <span class="more">READ MORE</span>
  </article>

  <footer class="panel footer">
    <span class="copy">© 2017 Kampfsportgilde Rheinau e.V.</span>
    <span class="legal">Impressum</span>
  </footer>

</div>
</body>
</html>
```